Qivera Health & Wellness Business Card Design

We would like to create business cards matching with our new logo design. The card should be professional looking but still have a playful side and something that would be eye catching. We are planing to open a luxury medical spa and looking to create a design based on this new logo. We are looking for a design that shows off luxury but not be gold in color. Also, while we are a more female oriented medical center we do have men that come in for our services and it should be be too feminine.

Target Market(s)

Health & Wellness. Medical patients. Luxury spa

Industry/Entity Type

Health And Wellness

Contact Information for Business Card

It should have the logo design in the front of card and back of card should have our contact information. Our current colors are peach/ coral, teal, and gray. We are looking for a modern looking design.

Font styles to use
Script

Colors
32a6d6
e667a6
86cfc6
fece3e

Requirements
Must have
• It should have our logo design. We would prefer to have a more modern look to the card.
Nice to have
• Eye-Catching Design on the personable side but still classy.
Should not have
• At this point we are looking for the best design. It should not have color purple.

```html
<!DOCTYPE html>
<html lang="en">
<head>
<meta charset="utf-8">
<title>Qivera Health &amp; Wellness – Business Card</title>
<link rel="stylesheet" href="https://fonts.googleapis.com/css2?family=Cinzel:wght@600&family=Tenor+Sans&display=swap">
<style>
  :root {
    --backdrop: #8c6f52;
    --band-gray: #e6e7ea;
    --coral: #f4958f;
    --slate-blue: #b0bfd3;
    --ink: #111111;
    --icon-disc: #e9e9eb;
  }
  * { margin: 0; padding: 0; box-sizing: border-box; }
  html, body { width: 900px; height: 1200px; overflow: hidden; }
  body {
    background: var(--backdrop);
    position: relative;
    font-family: "Tenor Sans", sans-serif;
    color: var(--ink);
  }
  .card {
    position: absolute;
    left: 86px;
    width: 736px;
    border-radius: 24px;
    overflow: hidden;
    box-shadow: 0 4px 10px rgba(0,0,0,0.35);
  }
  .card--contact { top: 137px; height: 428px; background: var(--coral); }
  .card--brand { top: 633px; height: 430px; background: var(--slate-blue); }

  .name-band {
    height: 153px;
    background: var(--band-gray);
    padding: 58px 0 0 51px;
  }
  .holder-name {
    font-family: "Cinzel", serif;
    font-weight: 600;
    font-size: 31px;
    letter-spacing: 0.5px;
  }
  .contact-list {
    list-style: none;
    position: absolute;
    left: 43px;
    top: 212px;
  }
  .contact-item {
    display: flex;
    align-items: center;
    height: 44px;
    margin-bottom: 19px;
    font-size: 22.5px;
  }
  .contact-icon {
    width: 44px; height: 44px;
    border-radius: 50%;
    background: var(--icon-disc);
    display: flex; align-items: center; justify-content: center;
    margin-right: 13px;
    flex: none;
  }
  .contact-icon svg { width: 22px; height: 22px; }

  .brand-name {
    position: absolute;
    text-align: center;
    font-family: "Tenor Sans", sans-serif;
    color: var(--ink);
    line-height: 1.15;
  }
  .brand-name .brand-word { display: block; }
  .card--contact .brand-name { left: 420px; top: 300px; width: 290px; }
  .card--contact .brand-word--main { font-size: 54px; }
  .card--contact .brand-word--sub { font-size: 19px; letter-spacing: 0.5px; }
  .card--brand .brand-name { left: 0; top: 150px; width: 736px; }
  .card--brand .brand-word--main { font-size: 76px; }
  .card--brand .brand-word--sub { font-size: 27px; letter-spacing: 0.5px; }
</style>
</head>
<body>
  <section class="card card--contact">
    <div class="name-band">
      <h1 class="holder-name">JOHNTHAN DOE</h1>
    </div>
    <ul class="contact-list">
      <li class="contact-item">
        <span class="contact-icon">
          <svg viewBox="0 0 24 24" aria-hidden="true"><path fill="#111" d="M6.6 2.5c.6-.3 1.3-.1 1.6.5l1.8 3.4c.3.6.1 1.2-.4 1.6L8.3 9c.9 2.6 3 5 5.6 6.3l1.1-1.3c.4-.5 1.1-.6 1.6-.3l3.2 2c.6.3.8 1 .5 1.6l-1 1.9c-.4.8-1.3 1.2-2.2 1C9.6 18.7 4.7 12.8 4 6.2c-.1-.9.3-1.7 1-2.2z"/></svg>
        </span>
        012 345 6789
      </li>
      <li class="contact-item">
        <span class="contact-icon">
          <svg viewBox="0 0 24 24" aria-hidden="true"><rect x="2.5" y="5.5" width="19" height="13" rx="1" fill="#111"/><path d="M3 6.5l9 6.5 9-6.5" stroke="#e9e9eb" stroke-width="1.6" fill="none"/></svg>
        </span>
        contact@Qiverahealth.com
      </li>
      <li class="contact-item">
        <span class="contact-icon">
          <svg viewBox="0 0 24 24" aria-hidden="true" fill="none" stroke="#111" stroke-width="1.7"><circle cx="12" cy="12" r="9.5"/><ellipse cx="12" cy="12" rx="4" ry="9.5"/><path d="M2.5 12h19M4 7h16M4 17h16"/></svg>
        </span>
        Qiverahealth.com
      </li>
    </ul>
    <p class="brand-name">
      <span class="brand-word brand-word--main">Qivera</span>
      <span class="brand-word brand-word--sub">Health &amp; Wellness</span>
    </p>
  </section>

  <section class="card card--brand">
    <p class="brand-name">
      <span class="brand-word brand-word--main">Qivera</span>
      <span class="brand-word brand-word--sub">Health &amp; Wellness</span>
    </p>
  </section>
</body>
</html>
```